Derek Milbourne needs a single album cover

I need an single album cover for a song I wrote called "Still Harbor". I would like the design to Illustrate how gods grace covers all sin.

Requirements
Must have
• The song title "Still Harbor" And my name Derek Milbourne

```html
<!DOCTYPE html>
<html lang="en">
<head>
<meta charset="utf-8">
<title>Still Harbor — Derek Milbourne</title>
<link href="https://fonts.googleapis.com/css2?family=Italianno&family=Josefin+Sans:wght@300&display=swap" rel="stylesheet">
<style>
  :root {
    --page-bg: #e9e6e1;
    --title-cream: #efe3a6;
    --name-gold: #e6d36a;
    --sky-deep: #173d27;
    --sky-green: #3f7436;
    --sky-olive: #7d8a2c;
    --sunset-amber: #e3a12f;
    --sunset-orange: #c8641f;
    --ground-dark: #0b0b07;
  }
  html, body {
    margin: 0;
    width: 1200px;
    height: 926px;
    overflow: hidden;
    background: var(--page-bg);
  }
  .album-cover {
    position: absolute;
    left: 170px;
    top: 33px;
    width: 860px;
    height: 860px;
    overflow: hidden;
    box-shadow: 0 10px 30px rgba(0,0,0,0.25);
  }
  .cover-scene {
    position: absolute;
    inset: 0;
    width: 100%;
    height: 100%;
  }
  .song-title {
    position: absolute;
    top: 62px;
    left: 0;
    width: 100%;
    padding-left: 120px;
    box-sizing: border-box;
    text-align: center;
    font-family: "Italianno", cursive;
    font-size: 92px;
    line-height: 1;
    color: var(--title-cream);
    margin: 0;
    font-weight: 400;
  }
  .artist-name {
    position: absolute;
    right: 90px;
    bottom: 58px;
    margin: 0;
    font-family: "Josefin Sans", sans-serif;
    font-weight: 300;
    font-size: 34px;
    letter-spacing: 4px;
    color: var(--name-gold);
    text-transform: uppercase;
  }
</style>
</head>
<body>
  <main class="album-cover">
    <svg class="cover-scene" viewBox="0 0 860 860" role="img" aria-label="Photograph of a sunset sky with glowing golden clouds over a dark hillside, with the silhouette of a man kneeling in prayer on the right">
      <defs>
        <linearGradient id="sky" x1="0" y1="0" x2="0" y2="1">
          <stop offset="0" stop-color="var(--sky-deep)"/>
          <stop offset="0.35" stop-color="var(--sky-green)"/>
          <stop offset="0.58" stop-color="var(--sky-olive)"/>
          <stop offset="0.74" stop-color="var(--sunset-amber)"/>
          <stop offset="0.82" stop-color="var(--sunset-orange)"/>
          <stop offset="0.86" stop-color="var(--ground-dark)"/>
          <stop offset="1" stop-color="var(--ground-dark)"/>
        </linearGradient>
        <radialGradient id="glow" cx="0.5" cy="0.76" r="0.45">
          <stop offset="0" stop-color="#fff0a8" stop-opacity="0.6"/>
          <stop offset="1" stop-color="#fff0a8" stop-opacity="0"/>
        </radialGradient>
      </defs>
      <rect width="860" height="860" fill="url(#sky)"/>
      <rect width="860" height="860" fill="url(#glow)"/>
    </svg>
    <h1 class="song-title">Still Harbor</h1>
    <p class="artist-name">Derek Milbourne</p>
  </main>
</body>
</html>
```